Debt Collection Website Design! We are the solution for landlords to get paid what they are owed.

We are a 3rd party debt collection company that specializes in Residential and Commercial real estate debt collection. We help landlords recover money from past residents by being fair, friendly and aggressive. We also collect/buy/sell/trade civil judgments won resulting from anything from automobile accidents to evictions to a pet zebra getting stolen. We buy single judgments to large portfolios, we also collect judgments for a nominal fee.

I would like a new, modern, easy to navigate website. A spot that we can post news stories or updated information about our company. I have included our company logo that must be on the top of the page. Feel free to ask any questions that will help get the process going.

Target Market(s)

Landlords, small to large apartment complex. Real estate services and lawyers.

Industry/Entity Type

Real Estate

Number of Pages Required

3 page

Requirements
Must have
• Company logo which has been attached. A page where we can explain the collection process, fees and placement. A page where we can explain judgments, collection vs. selling, placement form. I am open to any font/designs and willing to work with anyone.
Nice to have
• Nice to have a spot on the homepage to place news articles about ourselves and our industry.
Should not have
• I don't want it over crowded. Simple, sleek and easy to navigate is best. No gavels on any of the pages. It cannot look legal, say/show anything that we use legal powers to collect. We are not a law office, we don't practice law, we are 3rd party debt collection agency.

```html
<!DOCTYPE html>
<html lang="en">
<head>
<meta charset="utf-8">
<title>Ardent Recovery, LLC</title>
<link rel="stylesheet" href="https://fonts.googleapis.com/css2?family=Open+Sans:ital,wght@0,400;0,600;0,700;1,400&family=Raleway:wght@400;500;600&display=swap">
<style>
:root{
  --navy:#0b3a8c;
  --navy-dark:#082c6b;
  --blue:#1c55b3;
  --ink:#222;
  --muted:#666;
  --line:#dcdcdc;
  --white:#fff;
  --black:#000;
  --footer:#050505;
}
*{box-sizing:border-box;margin:0;padding:0}
html,body{width:1200px;height:2628px;overflow:hidden}
body{font-family:"Open Sans",Arial,sans-serif;color:var(--ink);background:var(--white);font-size:13px;line-height:1.5}
a{color:inherit;text-decoration:none}

/* header */
.site-header{height:123px;position:relative;background:var(--white)}
.brand{position:absolute;left:88px;top:18px;display:flex;align-items:center;gap:16px}
.brand-mark{width:78px;height:78px;background:var(--navy)}
.brand-name{font-family:"Open Sans",Arial,sans-serif;font-weight:600;color:var(--navy);font-size:34px;line-height:1.05;letter-spacing:1px;text-transform:uppercase}
.brand-name small{display:block;font-size:27px;letter-spacing:2px}
.call{position:absolute;right:88px;top:16px;text-align:right;color:var(--navy);font-weight:700;font-size:22px;line-height:1.1}
.call span{display:block;font-weight:400;font-size:26px}
.main-nav{position:absolute;left:686px;top:80px;display:flex;gap:44px;font-size:16px;color:#444}
.main-nav a.active{color:var(--navy);font-weight:600}

/* hero */
.hero{height:432px;position:relative;background:linear-gradient(100deg,#3b3b3b 0%,#6b6b6b 40%,#8a8a8a 65%,#4a4a4a 100%);color:var(--white);text-align:center}
.hero-photo{position:absolute;inset:0;background:radial-gradient(ellipse at 30% 70%,rgba(20,20,20,.55),transparent 60%),radial-gradient(ellipse at 80% 20%,rgba(230,230,230,.25),transparent 55%)}
.hero-content{position:relative;padding-top:145px}
.hero h1{font-family:"Raleway",sans-serif;font-weight:500;font-size:42px;letter-spacing:1px}
.hero p{font-size:13px;font-weight:600;margin-top:8px;letter-spacing:.5px}
.btn-outline{display:inline-block;margin-top:22px;border:2px solid var(--white);padding:5px 22px;font-size:12px;font-weight:600;background:rgba(0,0,0,.35)}

/* services */
.services{height:335px;text-align:center;padding-top:26px}
.section-title{font-family:"Raleway",sans-serif;font-weight:500;color:var(--blue);font-size:29px}
.section-sub{color:var(--blue);font-style:italic;font-size:15px}
.service-grid{display:flex;justify-content:space-between;width:1030px;margin:36px auto 0}
.service{width:220px}
.service svg{width:38px;height:38px;fill:var(--navy)}
.service h3{font-weight:400;font-size:17px;margin-top:4px}
.service p{font-size:12.5px;color:#333;line-height:1.45;margin-top:4px}
.service .more{display:block;margin-top:14px;color:var(--navy);font-size:13px}

/* feature band */
.feature{height:497px;background:var(--navy);color:var(--white);position:relative}
.feature-main{position:absolute;left:102px;top:42px;width:774px}
.feature-main h2{font-size:22px;font-weight:700;border-bottom:1px solid rgba(255,255,255,.6);padding-bottom:10px;width:440px}
.feature-main > p{font-size:12.5px;line-height:1.75;margin-top:14px}
.feature-media{display:flex;gap:22px;margin-top:44px}
.money-photo{width:380px;height:172px;flex:none;background:linear-gradient(120deg,#7ea7d8 0%,#c9a27a 45%,#8a6a4f 75%,#dfe6f0 100%)}
.feature-media p{font-size:12.5px;line-height:1.75}
.feature-media .more{display:block;margin-top:12px;font-size:12px;color:#c9d6f0}
.sidebar{position:absolute;left:905px;top:44px;width:210px}
.sidebar h4{font-size:17px;font-weight:400;margin-bottom:8px}
.side-list{list-style:none;font-size:10.5px}
.side-list li{border-bottom:1px solid rgba(255,255,255,.4);padding:3px 8px;line-height:17px;white-space:nowrap;overflow:hidden}
.side-list li.current{background:var(--white);color:var(--navy)}
.sidebar h4.second{margin-top:22px}

/* news & blog */
.news-blog{height:628px;position:relative}
.news{position:absolute;left:88px;top:28px;width:302px}
.block-title{font-size:26px;color:var(--navy);font-weight:400;padding-bottom:10px;border-bottom:2px solid var(--navy)}
.news-item{display:flex;gap:14px;height:125px;padding-top:22px;border-bottom:1px solid var(--line)}
.news-thumb{width:80px;height:80px;flex:none;background:linear-gradient(160deg,#b9c6d8,#5b6b82)}
.news-item h5{font-size:12.5px;font-weight:700}
.news-item p{font-size:11.5px;color:var(--muted);font-style:italic;line-height:1.4}
.meta{display:flex;gap:20px;margin-top:12px;font-size:11.5px;color:var(--navy)}
.meta span::before{content:"";display:inline-block;width:9px;height:9px;border:1px solid #999;border-radius:50%;margin-right:6px;vertical-align:-1px}
.blog{position:absolute;left:467px;top:28px;width:648px}
.post{display:flex;gap:24px;height:263px;padding-top:20px;border-bottom:1px solid var(--line)}
.post-photo{width:257px;height:190px;flex:none;border:1px solid #ccc}
.post-photo.savings{background:linear-gradient(120deg,#f1d5d2 0%,#e7b9b4 40%,#c8ccd4 70%,#9aa3b1 100%)}
.post-photo.house{background:linear-gradient(150deg,#e9edf2 0%,#8a96a8 50%,#3f4a5c 100%)}
.post-body{position:relative;flex:1}
.post h3{font-size:25px;font-weight:400;color:var(--navy);line-height:1.1}
.post .lead{font-size:12.5px;font-style:italic;color:#333;margin-top:8px}
.post .body{font-size:11.5px;line-height:1.6;margin-top:6px;color:#333}
.post .date{position:absolute;left:0;bottom:26px;font-size:14px}
.post .more{position:absolute;right:0;bottom:26px;font-size:11.5px;color:var(--navy)}

/* testimonials */
.testimonials{height:423px;background:linear-gradient(120deg,#1d1d1d 0%,#3d3d3d 45%,#262626 100%);color:var(--white);text-align:center;position:relative}
.testimonials h2{font-size:24px;font-weight:400;padding-top:140px}
.testimonials h2::after{content:"";display:block;width:90px;height:2px;background:var(--white);margin:10px auto 0}
.testimonials p{width:900px;margin:18px auto 0;font-size:13px;line-height:1.65;color:#ddd}
.dots{position:absolute;left:0;right:0;top:380px;display:flex;justify-content:center;gap:14px}
.dots i{width:46px;height:4px;background:#777}
.dots i.on{background:var(--white)}

/* footer */
.site-footer{height:190px;background:var(--footer);color:var(--white);text-align:center;padding-top:32px;font-size:13px}
.social{display:flex;justify-content:center;gap:12px}
.social i{width:38px;height:38px;border-radius:50%;background:var(--white)}
.site-footer p{margin-top:10px;line-height:1.5}
.site-footer .footer-nav{margin-top:10px}
</style>
</head>
<body>
<header class="site-header">
  <div class="brand">
    <div class="brand-mark"></div>
    <div class="brand-name">Ardent<small>Recovery, LLC</small></div>
  </div>
  <div class="call">call us Today<span>555 0134 27</span></div>
  <nav class="main-nav">
    <a class="active" href="#">Home</a><a href="#">About us</a><a href="#">News</a><a href="#">Stories</a><a href="#">Contact Us</a>
  </nav>
</header>

<section class="hero">
  <div class="hero-photo" role="img" aria-label="Photo of hands working a calculator and writing on paperwork"></div>
  <div class="hero-content">
    <h1>CLEAN AND MODERN DESIGN</h1>
    <p>LOREM IPSUM IS SIMPLY DUMMY TEXT OF</p>
    <a class="btn-outline" href="#">READ MORE</a>
  </div>
</section>

<section class="services">
  <h2 class="section-title">Lorem Ipsum is simply dummy text of the printing</h2>
  <p class="section-sub">Lorem Ipsum is simply</p>
  <div class="service-grid">
    <div class="service">
      <svg viewBox="0 0 40 40"><path d="M15 8h10l-3 5h-4z"/><path d="M17 13h6c7 4 10 11 9 16-1 5-6 7-12 7s-11-2-12-7c-1-5 2-12 9-16z"/><text x="20" y="31" font-size="12" text-anchor="middle" fill="#fff" font-family="Open Sans,sans-serif" font-weight="700">$</text></svg>
      <h3>Collect</h3>
      <p>Lorem Ipsum is simply dummy text of the printing and typesetting industry. Lorem Ipsum has been</p>
      <a class="more" href="#">Read More</a>
    </div>
    <div class="service">
      <svg viewBox="0 0 40 40"><path d="M20 4 36 12H4z"/><rect x="6" y="14" width="4" height="16"/><rect x="14" y="14" width="4" height="16"/><rect x="22" y="14" width="4" height="16"/><rect x="30" y="14" width="4" height="16"/><rect x="3" y="32" width="34" height="4"/></svg>
      <h3>Buy</h3>
      <p>Lorem Ipsum is simply dummy text of the printing and typesetting industry. Lorem Ipsum has been</p>
      <a class="more" href="#">Read More</a>
    </div>
    <div class="service">
      <svg viewBox="0 0 40 40"><ellipse cx="14" cy="30" rx="10" ry="4"/><ellipse cx="14" cy="24" rx="10" ry="4"/><ellipse cx="26" cy="18" rx="10" ry="4"/><ellipse cx="26" cy="12" rx="10" ry="4"/><ellipse cx="26" cy="6" rx="10" ry="4"/></svg>
      <h3>Sell</h3>
      <p>Lorem Ipsum is simply dummy text of the printing and typesetting industry. Lorem Ipsum has been</p>
      <a class="more" href="#">Read More</a>
    </div>
    <div class="service">
      <svg viewBox="0 0 40 40"><path d="M4 14 14 6v5h14v6H14v5z"/><path d="M36 26 26 34v-5H12v-6h14v-5z"/></svg>
      <h3>Trade</h3>
      <p>Lorem Ipsum is simply dummy text of the printing and typesetting industry. Lorem Ipsum has been</p>
      <a class="more" href="#">Read More</a>
    </div>
  </div>
</section>

<section class="feature">
  <div class="feature-main">
    <h2>Lorem Ipsum is simply</h2>
    <p>Lorem Ipsum is simply dummy text of the printing and typesetting industry. Lorem Ipsum has been the industry's standard dummy text ever since the 1500s, when an unknown printer took a galley of type and scrambled it to make a type specimen book. It has survived not only five centuries, but also the leap into electronic typesetting, remaining essentially unchanged. It was popularised in the 1960s with the release of Pressline sheets containing Lorem Ipsum passages, and more recently with desktop publishing software like Quillset Layout including versions of Lorem Ipsum. Contrary to popular belief, Lorem Ipsum is not simply random text. It has roots in a piece of classical Latin literature from 45 BC, making it over 2000 years old. Edwin Harrow, a Latin professor at Westbrook College in Virginia</p>
    <div class="feature-media">
      <div class="money-photo" role="img" aria-label="Photo of a fanned stack of banknotes"></div>
      <div>
        <p>Lorem Ipsum is simply dummy text of the printing and typesetting industry. Lorem Ipsum has been the industry's standard dummy text ever since the 1500s, when an unknown printer took a galley of type and scrambled it to make a type specimen book. It has survived not only five centuries, but also the leap into electronic typesetting, remaining essentially unchanged. It was popularised in the 1960s with the release</p>
        <a class="more" href="#">Read More</a>
      </div>
    </div>
  </div>
  <aside class="sidebar">
    <h4>Market Place</h4>
    <ul class="side-list">
      <li class="current">Lorem Ipsum is simply</li>
      <li>It is a long established</li>
      <li>There are many variations</li>
      <li>Lorem Ipsum which looks reasonable</li>
      <li>The standard chunk of Lorem</li>
    </ul>
    <h4 class="second">Categories</h4>
    <ul class="side-list">
      <li class="current">Making this the first true</li>
      <li>From a Lorem Ipsum passage</li>
      <li>"Bonorum et Malorum" by Tullo</li>
      <li>It was popularised in the</li>
      <li>Looked up one of the more</li>
      <li>Lorem Ipsum</li>
      <li>Contrary to popular</li>
      <li>Many desktop publishing</li>
    </ul>
  </aside>
</section>

<section class="news-blog">
  <div class="news">
    <h2 class="block-title">Latest News</h2>
    <article class="news-item"><div class="news-thumb" role="img" aria-label="Portrait thumbnail of the article author"></div><div><h5>Utlit amet risus acur venenat</h5><p>Proliet adiunt dolor sit amet consectetur adipiscing elit sed do eiusmod</p><div class="meta"><span>Alan Porter</span><span>o Comments</span></div></div></article>
    <article class="news-item"><div class="news-thumb" role="img" aria-label="Portrait thumbnail of the article author"></div><div><h5>Utlit amet risus acur venenat</h5><p>Proliet adiunt dolor sit amet consectetur adipiscing elit sed do eiusmod</p><div class="meta"><span>Alan Porter</span><span>o Comments</span></div></div></article>
    <article class="news-item"><div class="news-thumb" role="img" aria-label="Portrait thumbnail of the article author"></div><div><h5>Utlit amet risus acur venenat</h5><p>Proliet adiunt dolor sit amet consectetur adipiscing elit sed do eiusmod</p><div class="meta"><span>Alan Porter</span><span>o Comments</span></div></div></article>
    <article class="news-item"><div class="news-thumb" role="img" aria-label="Portrait thumbnail of the article author"></div><div><h5>Utlit amet risus acur venenat</h5><p>Proliet adiunt dolor sit amet consectetur adipiscing elit sed do eiusmod</p><div class="meta"><span>Alan Porter</span><span>o Comments</span></div></div></article>
  </div>
  <div class="blog">
    <h2 class="block-title">Latest From Blog</h2>
    <article class="post">
      <div class="post-photo savings" role="img" aria-label="Photo of a piggy bank beside a small model house"></div>
      <div class="post-body">
        <h3>Lorem Ipsum is simply dummy</h3>
        <p class="lead">Lorem Ipsum is simply dummy</p>
        <p class="body">Lorem Ipsum is simply dummy text of the printing and typesetting industry. Lorem Ipsum has been the industry's standard dummy text ever since the 1500s, when an unknown printer took a galley of type and scrambled it to make a type specimen book. It has survived not only five centuries, but also the leap into electronic typesetting, remaining essentially unchanged. It was popularised in the 1960s with the release of Pressline sheets containing</p>
        <span class="date">Jan 05 , 2015</span><a class="more" href="#">Read More</a>
      </div>
    </article>
    <article class="post">
      <div class="post-photo house" role="img" aria-label="Photo of a model house with blue roof tiles"></div>
      <div class="post-body">
        <h3>Lorem Ipsum is simply dummy</h3>
        <p class="lead">Lorem Ipsum is simply dummy</p>
        <p class="body">Lorem Ipsum is simply dummy text of the printing and typesetting industry. Lorem Ipsum has been the industry's standard dummy text ever since the 1500s, when an unknown printer took a galley of type and scrambled it to make a type specimen book. It has survived not only five centuries, but also the leap into electronic typesetting, remaining essentially unchanged. It was popularised in the 1960s with the release of Pressline sheets containing</p>
        <span class="date">Jan 05 , 2015</span><a class="more" href="#">Read More</a>
      </div>
    </article>
  </div>
</section>

<section class="testimonials" role="img" aria-label="Dark background photo of a business handshake behind client testimonials">
  <h2>Client Testimonials</h2>
  <p>Lorem ipsum dolor sit amet, consectetuer adipiscing elit, sed diam nonummy nibh euismod tincidunt ut laoreet dolore magna aliquam erat volutpat. Ut wisi enim ad minim veniam, quis nostrud exerci tation ullamcorper suscipit lobortis nisl ut aliquip ex ea commodo consequat. Duis autem vel eum iriure dolor in hendrerit in vulputate velit esse molestie consequat, vel illum dolore eu feugiat nulla facilisis at vero eros et accumsan.</p>
  <div class="dots"><i></i><i class="on"></i><i></i></div>
</section>

<footer class="site-footer">
  <div class="social"><i></i><i></i><i></i><i></i></div>
  <p>Designed &amp; Developed By Northpine Studio<br>© 2014 ardentrecovery, all rights reserved</p>
  <div class="footer-nav">Home &nbsp;/&nbsp; Blog &nbsp;/&nbsp; About &nbsp;/&nbsp; Contact &nbsp;/&nbsp; Locations &nbsp;/&nbsp; Services &nbsp;/&nbsp; Privacy Policy</div>
</footer>
</body>
</html>
```